Simple and clean

We need a business card design for a new company called Dwelling Owl. It is a search engine to find current properties for sale or rent in New Zealand market.
We have already a colour scheme that we would like people to use.
Light brown: #D4CCB0
Light green: #D6E4D4
Green: #669966
Black/White
It is OK to divert from this colour scheme slightly as long as there is a green component to the business card.
Final design should be clean, simple and should communicate the nature of the business.
Target Market(s)
- First home buyers
- Real estate agents
- People seeking rentals
Industry/Entity Type
Business
Requirements
Must have
- Use those or similar colours.
Light brown: #D4CCB0
Light green: #D6E4D4
Green: #669966
Black/White

```html
<!DOCTYPE html>
<html lang="en">
<head>
<meta charset="utf-8">
<title>Dwelling Owl – Business Card</title>
<link rel="stylesheet" href="https://fonts.googleapis.com/css2?family=Arimo:wght@400;700&display=swap">
<style>
  :root {
    --backdrop: #333333;
    --card-white: #ffffff;
    --green: #669966;
    --green-light: #a3c59c;
    --text-grey: #555555;
    --rule-grey: #666666;
  }
  html, body {
    margin: 0;
    padding: 0;
    width: 1200px;
    height: 1200px;
    overflow: hidden;
    background: var(--backdrop);
  }
  .canvas {
    position: relative;
    width: 1200px;
    height: 1200px;
  }
  .business-card {
    position: absolute;
    left: 95px;
    top: 312px;
    width: 1010px;
    height: 576px;
    background: var(--card-white);
    overflow: hidden;
    font-family: "Arimo", Arial, sans-serif;
    color: var(--text-grey);
  }
  .accent-panel {
    position: absolute;
    left: 0;
    top: 0;
    width: 242px;
    height: 576px;
    background: linear-gradient(160deg, var(--green-light) 0%, var(--green) 100%);
  }
  .holder-name {
    position: absolute;
    left: 312px;
    top: 110px;
    margin: 0;
    font-size: 48px;
    font-weight: 400;
    line-height: 1;
  }
  .name-rule {
    position: absolute;
    left: 261px;
    top: 157px;
    width: 720px;
    height: 3px;
    background: var(--rule-grey);
  }
  .contact-list {
    position: absolute;
    left: 320px;
    top: 166px;
    margin: 0;
    padding: 0;
    list-style: none;
    font-size: 40px;
    line-height: 52px;
  }
  .contact-web {
    font-size: 33px;
    font-weight: 700;
    line-height: 40px;
  }
  .brand-mark {
    position: absolute;
    right: 30px;
    top: 483px;
    display: flex;
    align-items: center;
    gap: 12px;
  }
  .brand-dot {
    width: 56px;
    height: 56px;
    border-radius: 50%;
    background: var(--green);
  }
  .brand-name {
    font-size: 44px;
    font-weight: 400;
    color: var(--green);
    line-height: 1;
  }
</style>
</head>
<body>
<main class="canvas">
  <section class="business-card">
    <div class="accent-panel" role="img" aria-label="Decorative faceted green geometric band"></div>

    <h1 class="holder-name">Tom Reed</h1>
    <div class="name-rule"></div>
    <ul class="contact-list">
      <li class="contact-role">Developer</li>
      <li class="contact-phone">09312456</li>
      <li class="contact-email">tom@reedmail.com</li>
      <li class="contact-web">www.dwellingowl.co.nz</li>
    </ul>

    <div class="brand-mark">
      <span class="brand-dot"></span>
      <span class="brand-name">Dwelling Owl</span>
    </div>
  </section>
</main>
</body>
</html>
```